Unique Business Card Design

Unique Business Card design for our orthotic and prosthetic company. Our logo is on our website, color is light blue. Unique shape (artificial leg shaped, vertical, etc..) preferred. Logo, business name, individual name and basic demographics needed.

Industry/Entity Type

Business

Contact Information for Business Card

Logo, Industry, Phone # Logo, "Prosthetic & Orthotic Services" Place to add individual name and contact info

Colors
cee9f5

Requirements
Must have
• The icon must be there, placement of "Prosthetic & Orthotic Services" can be moved
Nice to have
• Like the mix of light blue, and a little darker blue. One design included the icons from my website which was a nice touch

```html
<!DOCTYPE html>
<html lang="en">
<head>
<meta charset="utf-8">
<title>Limbwell Inc. Business Card</title>
<link rel="stylesheet" href="https://fonts.googleapis.com/css2?family=Open+Sans:wght@600&family=Roboto:ital,wght@0,400;0,700;1,400&family=Tinos:ital@1&display=swap">
<style>
  :root {
    --brand-blue: #246397;
    --brand-blue-deep: #1f5a8c;
    --paper: #f4f4f4;
    --stage: #e4e4e4;
    --ink: #2b2b2b;
    --ink-soft: #4a4a4a;
    --white: #ffffff;
  }
  * { margin: 0; padding: 0; box-sizing: border-box; }
  html, body { width: 1200px; height: 576px; overflow: hidden; }
  body { background: var(--stage); position: relative; font-family: "Roboto", sans-serif; }

  .card { position: absolute; border-radius: 6px; }
  .card-front { left: 82px; top: 139px; width: 484px; height: 291px;
    background: linear-gradient(180deg, var(--brand-blue) 0%, var(--brand-blue-deep) 100%); }
  .card-back { left: 602px; top: 139px; width: 480px; height: 289px; background: var(--paper); }

  .brand-mark { position: absolute; border-radius: 50%; }
  .front-mark { left: 93px; top: 108px; width: 76px; height: 76px; background: var(--white); }
  .back-mark { left: 332px; top: 19px; width: 80px; height: 80px; background: var(--brand-blue); }

  .brand-name { position: absolute; font-family: "Open Sans", sans-serif; font-weight: 600; white-space: nowrap; }
  .front-name { left: 190px; top: 108px; font-size: 24px; color: var(--white); }
  .back-name { left: 372px; top: 102px; transform: translateX(-50%); font-size: 18px; color: var(--brand-blue); }

  .tagline { position: absolute; font-family: "Tinos", serif; font-style: italic; white-space: nowrap; }
  .front-tagline { left: 213px; top: 141px; font-size: 12.5px; color: var(--white); }
  .back-tagline { left: 372px; top: 130px; transform: translateX(-50%); font-size: 10px; color: var(--brand-blue); }

  .front-phone { position: absolute; left: 215px; top: 157px; font-family: "Open Sans", sans-serif;
    font-weight: 600; font-size: 21px; letter-spacing: 1px; color: var(--white); }

  .accent-bar { position: absolute; left: 0; top: 23px; width: 13px; height: 74px; background: var(--brand-blue); }
  .person-name { position: absolute; left: 32px; top: 28px; font-size: 19px; font-weight: 700; color: var(--brand-blue); }
  .person-title { position: absolute; left: 32px; top: 52px; font-size: 11px; font-style: italic; color: var(--ink-soft); }
  .person-mobile { position: absolute; left: 32px; top: 72px; display: flex; align-items: center; gap: 10px;
    font-size: 14px; color: var(--ink); }

  .contact-list { position: absolute; left: 38px; top: 175px; list-style: none; }
  .contact-list li { display: flex; align-items: center; height: 17px; font-size: 12px; color: var(--ink); }
  .contact-list svg { width: 11px; height: 11px; margin-right: 7px; fill: var(--brand-blue); }
  .address { position: absolute; left: 38px; top: 251px; font-size: 12px; color: var(--ink); }
</style>
</head>
<body>
  <section class="card card-front">
    <div class="brand-mark front-mark"></div>
    <div class="brand-name front-name">LIMBWELL INC.</div>
    <div class="tagline front-tagline">Prosthetic &amp; Orthotic Services</div>
    <div class="front-phone">718.555.0170</div>
  </section>

  <section class="card card-back">
    <div class="accent-bar"></div>
    <div class="person-name">Mara Ellison</div>
    <div class="person-title">Orthotist/Prosthetist</div>
    <div class="person-mobile">
      <svg width="10" height="14" viewBox="0 0 10 14"><rect x="0.5" y="0.5" width="9" height="13" rx="1.5" fill="var(--brand-blue)"/><rect x="2" y="2.5" width="6" height="8" fill="var(--paper)"/></svg>
      <span>845-555-0142</span>
    </div>

    <div class="brand-mark back-mark"></div>
    <div class="brand-name back-name">LIMBWELL INC.</div>
    <div class="tagline back-tagline">Prosthetic &amp; Orthotic Services</div>

    <ul class="contact-list">
      <li><svg viewBox="0 0 12 12"><path d="M1 4c0-2 2-3 5-3s5 1 5 3v1H8V4H4v1H1z"/><rect x="2" y="6" width="8" height="5" rx="1"/></svg>718.555.0170</li>
      <li><svg viewBox="0 0 12 12"><rect x="3" y="0.5" width="6" height="3"/><rect x="0.5" y="4" width="11" height="5" rx="1"/><rect x="3" y="8" width="6" height="3.5"/></svg>718.555.0139</li>
      <li><svg viewBox="0 0 12 12"><circle cx="6" cy="6" r="5.5"/><path d="M0.5 6h11M6 0.5v11" stroke="var(--paper)" stroke-width="0.8"/></svg>www.limbwellinc.com</li>
      <li><svg viewBox="0 0 12 12"><rect x="0.5" y="2" width="11" height="8"/><path d="M0.5 2l5.5 5 5.5-5" stroke="var(--paper)" stroke-width="0.9" fill="none"/></svg>mellison@limbwellinc.com</li>
    </ul>
    <div class="address">820 Harbor Ave. Riverton, NY 11900</div>
  </section>
</body>
</html>
```